Billboard Velmarhof - Maison K

I need two Billboards (125cm width x 340 height) -. They will be standing side by side in front of a building. Each billboard contains details of a business. 1. Medical center: VELMARHOF DRONSEL 2. Beauty saloon/Permanent make-up. MAISON K & ZOW Clinic. We already have a mockup. (see uploads). We want a design fitting the building with upmarket look. Modern, fresh and classy. The billboards need to have the same background color as in the mockup: dark-grey/black. The medical center has a green accent and the Beauty salon soft pink. The billboards should have certain uniformity.

Target Market(s)

Upmarket men and women

Font styles to use
Sans Serif

Requirements
Must have
• WE LIKE OUT OF THE BOX DESIGNS

VELMARHOF DRONSEL
Uw rug is onze zorg - this is the tagline
hello@velmarhofdronsel.be
09 614 28 90
www.velmarhofdronsel.be
facebook icon | instagram icon

MAISON K (HAS TWO DEPARTMENTS)
1. Schoonheidsinstituut - (which means beauty salon)
2. ZOW clinic (which means permanent make up)
0486 91 37 52
hello@maisonk.be
www.maisonk.be

hello@maisonk.be
Should not have
• not curly, not kitch, no color-books
NO PICTURES IN DESIGN

```html
<!DOCTYPE html>
<html lang="nl">
<head>
<meta charset="utf-8">
<title>Billboards Velmarhof Dronsel en Maison K</title>
<link rel="stylesheet" href="https://fonts.googleapis.com/css2?family=Roboto:wght@300;400&display=swap">
<style>
  :root {
    --wall: #e8e7e5;
    --black: #000000;
    --charcoal: #131215;
    --white: #ffffff;
    --silver: #a9a9a9;
    --green: #7dc24f;
    --pink: #f19aa8;
    --font: "Roboto", sans-serif;
  }
  * { margin: 0; padding: 0; box-sizing: border-box; }
  html, body { width: 919px; height: 1200px; overflow: hidden; background: var(--wall); }
  body { position: relative; font-family: var(--font); font-weight: 300; color: var(--white); }

  .billboard { position: absolute; width: 407px; top: 46px; height: 1106px; background: var(--charcoal); overflow: hidden; }
  .billboard--medical { left: 36px; --accent: var(--green); }
  .billboard--beauty { left: 477px; --accent: var(--pink); }

  .section { position: absolute; left: 0; width: 100%; }
  .section--brand { top: 0; height: 297px; background: var(--black); }
  .section--tagline { top: 297px; height: 60px; background: var(--black); display: flex; align-items: center; justify-content: center; }
  .section--social { top: 599px; height: 56px; background: var(--black); display: flex; align-items: center; justify-content: center; gap: 24px; }

  .rule { position: absolute; left: 0; width: 100%; height: 2px;
    background: linear-gradient(90deg, #5a5a5a, #d8d8d8 45%, #f2f2f2 50%, #d8d8d8 55%, #5a5a5a); }

  .tagline { font-size: 27px; font-weight: 400; letter-spacing: -0.3px; color: var(--silver); white-space: nowrap; }

  .brand-mark { position: absolute; left: 50%; transform: translateX(-50%); border-radius: 50%; }
  .brand-name { position: absolute; left: 0; width: 100%; text-align: center; font-weight: 400; color: var(--white); white-space: nowrap; }

  .billboard--medical .brand-mark { top: 76px; width: 76px; height: 76px; border: 2px solid var(--green); }
  .billboard--medical .brand-name { top: 168px; font-size: 44px; line-height: 46px; letter-spacing: 1px; }
  .brand-name__sub { display: block; font-size: 31px; line-height: 36px; letter-spacing: 1.5px; }

  .billboard--beauty .brand-mark { top: 79px; width: 84px; height: 84px; border: 2px solid var(--white); }
  .billboard--beauty .brand-name { top: 192px; font-size: 27px; letter-spacing: 17px; padding-left: 17px; font-weight: 300; }
  .brand-descriptor { position: absolute; top: 238px; left: 0; width: 100%; text-align: center; font-size: 8px; font-weight: 400; letter-spacing: 8.4px; padding-left: 8px; color: var(--white); }

  .contact { position: absolute; left: 0; width: 100%; text-align: center; }
  .contact__icon { display: block; margin: 0 auto; width: 20px; height: 20px; stroke: var(--accent); fill: none; stroke-width: 1.8; stroke-linecap: round; stroke-linejoin: round; }
  .contact__text { display: block; font-size: 17px; line-height: 20px; color: var(--white); margin-top: 6px; }
  .contact__text--web { font-size: 22px; line-height: 26px; color: var(--accent); margin-top: 4px; }

  .social-dot { width: 31px; height: 31px; border-radius: 50%; background: var(--accent); }

  .clinic { position: absolute; left: 0; width: 100%; text-align: center; white-space: nowrap; }
  .clinic__name { top: 702px; font-size: 38px; letter-spacing: 10px; padding-left: 10px; font-weight: 300; }
  .clinic__byline { top: 794px; font-size: 10px; letter-spacing: 3.2px; font-weight: 400; }
  .clinic__service { top: 834px; font-size: 27px; font-weight: 400; color: var(--silver); letter-spacing: -0.3px; }
  .clinic__web { top: 930px; font-size: 22px; color: var(--pink); }
</style>
</head>
<body>

<section class="billboard billboard--medical" aria-label="Velmarhof Dronsel">
  <div class="section section--brand">
    <div class="brand-mark" aria-hidden="true"></div>
    <h1 class="brand-name">VELMARHOF<span class="brand-name__sub">DRONSEL</span></h1>
  </div>
  <div class="rule" style="top:296px"></div>
  <div class="section section--tagline"><p class="tagline">UW RUG IS ONZE ZORG</p></div>
  <div class="rule" style="top:356px"></div>

  <div class="contact" style="top:390px">
    <svg class="contact__icon" viewBox="0 0 24 24" aria-hidden="true"><rect x="3" y="5" width="18" height="14" rx="1"/><path d="M8 10l4 3 4-3"/></svg>
    <span class="contact__text">hello@velmarhofdronsel.be</span>
  </div>
  <div class="contact" style="top:453px">
    <svg class="contact__icon" viewBox="0 0 24 24" aria-hidden="true"><path d="M5 4h4l2 5-2.5 1.5a11 11 0 0 0 5 5L15 13l5 2v4a2 2 0 0 1-2 2A16 16 0 0 1 3 6a2 2 0 0 1 2-2z"/><path d="M14 3a7 7 0 0 1 7 7M14 7a3 3 0 0 1 3 3"/></svg>
    <span class="contact__text">09 614 28 90</span>
  </div>
  <div class="contact" style="top:522px">
    <svg class="contact__icon" viewBox="0 0 24 24" aria-hidden="true"><circle cx="12" cy="12" r="9"/><path d="M3 12h18M12 3c3 3 3 15 0 18M12 3c-3 3-3 15 0 18"/></svg>
    <span class="contact__text contact__text--web">www.velmarhofdronsel.be</span>
  </div>

  <div class="rule" style="top:598px"></div>
  <div class="section section--social" role="img" aria-label="Sociale media">
    <span class="social-dot"></span>
    <span class="social-dot"></span>
  </div>
  <div class="rule" style="top:654px"></div>
</section>

<section class="billboard billboard--beauty" aria-label="Maison K">
  <div class="section section--brand">
    <div class="brand-mark" aria-hidden="true"></div>
    <h1 class="brand-name">MAISON K</h1>
    <p class="brand-descriptor">SCHOONHEIDSINSTITUUT</p>
  </div>
  <div class="rule" style="top:296px"></div>
  <div class="section section--tagline"><p class="tagline">SCHOONHEIDSINSTITUUT</p></div>
  <div class="rule" style="top:356px"></div>

  <div class="contact" style="top:388px">
    <svg class="contact__icon" viewBox="0 0 24 24" aria-hidden="true"><rect x="3" y="5" width="18" height="14" rx="1"/><path d="M8 10l4 3 4-3"/></svg>
    <span class="contact__text">hello@maisonk.be</span>
  </div>
  <div class="contact" style="top:450px">
    <svg class="contact__icon" viewBox="0 0 24 24" aria-hidden="true"><path d="M5 4h4l2 5-2.5 1.5a11 11 0 0 0 5 5L15 13l5 2v4a2 2 0 0 1-2 2A16 16 0 0 1 3 6a2 2 0 0 1 2-2z"/><path d="M14 3a7 7 0 0 1 7 7M14 7a3 3 0 0 1 3 3"/></svg>
    <span class="contact__text">0486 91 37 52</span>
  </div>
  <div class="contact" style="top:518px">
    <svg class="contact__icon" viewBox="0 0 24 24" aria-hidden="true"><circle cx="12" cy="12" r="9"/><path d="M3 12h18M12 3c3 3 3 15 0 18M12 3c-3 3-3 15 0 18"/></svg>
    <span class="contact__text contact__text--web">www.maisonk.be</span>
  </div>

  <div class="rule" style="top:598px"></div>
  <div class="section section--social" role="img" aria-label="Sociale media">
    <span class="social-dot"></span>
    <span class="social-dot"></span>
    <span class="social-dot"></span>
  </div>
  <div class="rule" style="top:654px"></div>

  <h2 class="clinic clinic__name">ZOW CLINIC</h2>
  <p class="clinic clinic__byline">PERMANENT MAKE UP BY NOOR VANDAELE</p>
  <p class="clinic clinic__service">PERMANENT MAKE UP</p>
  <p class="clinic clinic__web">www.zowclinic.be</p>
</section>

</body>
</html>
```